PSD for an Italian pizza restaurant web site.

I need an PSD for a Italian pizza restaurant web site.
I have all the php coding work done I just need the front end layout.
I have attached the logo.
Colors to be used
Black
Green
Red
White
Must have navigation buttons across header under logo and left column.
No other requirements!!
Anything Goes!!
Thoughts or ideals:
Fading colors
Textured back ground.
maybe old paper look
Italian flag
The restaurant food includes
pizza, pasta, salads and sandwiches
The restaurant is not a fast food restaurant.
Its a finer dining restaurant.
The current website is extremely bad.
http://www.brunellotrattoria.com/

```html
<!DOCTYPE html>
<html lang="en">
<head>
<meta charset="utf-8">
<title>Brunello's Italian Restaurant</title>
<link href="https://fonts.googleapis.com/css2?family=Bebas+Neue&family=Oswald:wght@400;500&family=Arimo:wght@400&family=Varela+Round&display=swap" rel="stylesheet">
<style>
  :root{
    --wood-dark:#2a0f07;
    --wood-mid:#5a2612;
    --wood-light:#6e3118;
    --paper:#ece3cf;
    --paper-edge:#d9ccb0;
    --tag:#eadbb9;
    --red:#a8141a;
    --red-deep:#8a0d12;
    --gold:#e0a22a;
    --ink:#141210;
    --text:#2b2520;
    --white:#ffffff;
    --strip:#7a3a17;
  }
  *{margin:0;padding:0;box-sizing:border-box}
  html,body{width:1200px;height:675px;overflow:hidden}
  body{
    position:relative;
    background:
      repeating-linear-gradient(90deg, rgba(0,0,0,.25) 0 2px, transparent 2px 150px),
      radial-gradient(ellipse at 50% 45%, var(--wood-light) 0%, var(--wood-mid) 45%, var(--wood-dark) 100%);
    font-family:"Arimo", Arial, sans-serif;
  }
  .sheet{
    position:absolute;left:263px;top:80px;width:684px;height:560px;
    background:radial-gradient(ellipse at 50% 40%, var(--paper) 55%, var(--paper-edge) 100%);
    box-shadow:0 6px 18px rgba(0,0,0,.55);
  }
  .sheet-holes{position:absolute;left:0;top:0}
  .torn-edge{position:absolute;left:263px;top:630px}
  .tag{
    position:absolute;left:244px;top:8px;width:176px;height:222px;
    background:var(--tag);
    clip-path:polygon(18% 0,82% 0,100% 14%,100% 100%,0 100%,0 14%);
    transform:rotate(-3deg);
    box-shadow:0 4px 10px rgba(0,0,0,.5);
    text-align:center;
  }
  .tag-hole{position:absolute;left:80px;top:10px;width:14px;height:14px;border-radius:50%;background:var(--wood-mid)}
  .tag-dot{position:absolute;left:70px;top:48px;width:36px;height:36px;border-radius:50%;background:var(--red)}
  .tag-name{position:absolute;left:0;right:0;top:108px;font-family:"Bebas Neue",sans-serif;font-size:38px;line-height:1;color:var(--ink);white-space:nowrap}
  .tag-sub{position:absolute;left:0;right:0;top:148px;font-family:"Bebas Neue",sans-serif;font-size:19px;line-height:1;color:var(--ink);white-space:nowrap}
  .main-nav{
    position:absolute;left:483px;top:130px;width:464px;height:43px;
    background:linear-gradient(90deg,#5b2a10,var(--strip) 30%,#8a4a20 60%,#6a3013);
    display:flex;justify-content:space-around;align-items:center;padding:0 6px;
  }
  .main-nav a{font-family:"Oswald",sans-serif;font-style:italic;font-size:17px;color:var(--white);text-decoration:none;text-transform:uppercase;letter-spacing:.5px}
  .hero-title{position:absolute;left:328px;top:250px;font-family:"Bebas Neue",sans-serif;font-weight:400;font-size:58px;line-height:1;color:var(--red);white-space:nowrap}
  .hero-tagline{position:absolute;left:322px;top:320px;font-family:"Bebas Neue",sans-serif;font-size:50px;line-height:1;color:var(--ink);white-space:nowrap}
  .hero-tagline span{color:var(--gold)}
  .hero-copy{position:absolute;left:324px;top:378px;width:378px;font-size:11.5px;line-height:1.45;color:var(--text)}
  .pizza-photo{
    position:absolute;left:712px;top:210px;width:270px;height:228px;border-radius:50%;
    background:radial-gradient(circle at 50% 45%, #c4561e 0%, #b0401a 45%, #d9a24a 80%, #c88a3a 100%);
    box-shadow:0 6px 10px rgba(0,0,0,.35);
  }
  .promo-row{position:absolute;left:272px;top:453px;width:660px;height:104px;display:flex;gap:4px}
  .promo{
    position:relative;flex:none;height:104px;
    background:linear-gradient(180deg,var(--red) 0%,var(--red-deep) 100%);
    color:var(--white);font-family:"Varela Round",sans-serif;text-decoration:none;
  }
  .promo-order{width:196px}
  .promo-party{width:246px}
  .promo-specials{width:210px}
  .promo-label{position:absolute;left:16px;top:16px;line-height:.95;white-space:nowrap}
  .promo .big{font-size:30px;display:block}
  .promo .small{font-size:13px;display:block}
  .promo .name{font-size:21px;display:block}
  .promo .mid{font-size:19px;display:block}
  .promo .cta{font-size:12px;display:block;margin-top:6px}
  .promo svg{position:absolute}
  .footer-nav{position:absolute;left:276px;top:573px;display:flex;gap:14px}
  .footer-nav a,.copyright,.contact-line{font-family:"Oswald",sans-serif;font-size:10px;color:var(--ink);text-decoration:none;text-transform:uppercase}
  .copyright{position:absolute;left:276px;top:590px}
  .contact-block{position:absolute;right:267px;top:569px;text-align:right;font-style:normal}
  .contact-line{display:block;line-height:2}
</style>
</head>
<body>
  <div class="sheet">
    <svg class="sheet-holes" width="684" height="30" aria-hidden="true">
      <g fill="#3a180b">
        <circle cx="20" cy="18" r="6"/><circle cx="48" cy="18" r="6"/><circle cx="76" cy="18" r="6"/><circle cx="104" cy="18" r="6"/><circle cx="132" cy="18" r="6"/><circle cx="160" cy="18" r="6"/><circle cx="188" cy="18" r="6"/><circle cx="216" cy="18" r="6"/><circle cx="244" cy="18" r="6"/><circle cx="272" cy="18" r="6"/><circle cx="300" cy="18" r="6"/><circle cx="328" cy="18" r="6"/><circle cx="356" cy="18" r="6"/><circle cx="384" cy="18" r="6"/><circle cx="412" cy="18" r="6"/><circle cx="440" cy="18" r="6"/><circle cx="468" cy="18" r="6"/><circle cx="496" cy="18" r="6"/><circle cx="524" cy="18" r="6"/><circle cx="552" cy="18" r="6"/><circle cx="580" cy="18" r="6"/><circle cx="608" cy="18" r="6"/><circle cx="636" cy="18" r="6"/><circle cx="664" cy="18" r="6"/>
      </g>
    </svg>
  </div>
  <svg class="torn-edge" width="684" height="20" aria-hidden="true">
    <path d="M0 0H684V8L668 14 650 6 630 16 612 8 590 15 570 6 548 14 526 7 504 16 482 8 460 14 438 6 416 15 394 8 372 16 350 6 328 14 306 8 284 16 262 7 240 14 218 6 196 15 174 8 152 16 130 6 108 14 86 8 64 16 42 7 20 14 0 6Z" fill="var(--paper-edge)"/>
  </svg>

  <div class="tag">
    <span class="tag-hole"></span>
    <span class="tag-dot"></span>
    <div class="tag-name">BRUNELLO'S</div>
    <div class="tag-sub">ITALIAN RESTAURANT</div>
  </div>

  <nav class="main-nav">
    <a href="#">Home</a><a href="#">Menu</a><a href="#">Specials</a><a href="#">Coupons</a><a href="#">Locations</a><a href="#">Contact</a>
  </nav>

  <h1 class="hero-title">BRUNELLO'S PIZZA</h1>
  <p class="hero-tagline">“ WE TOP ALL <span>PIZZAS</span>”</p>
  <p class="hero-copy">We Believe Our Pizza Is The Very Best! Our dough is made fresh daily, we buy the highest quality cheese and toppings, our vegetables are fresh and never frozen. This is why we believe our pizza is the very best.</p>

  <div class="pizza-photo" role="img" aria-label="Photo of a whole pizza with mushrooms and herbs, one slice pulled out"></div>

  <div class="promo-row">
    <a class="promo promo-order" href="#">
      <span class="promo-label"><span class="big">order<br>online</span><span class="cta">click here ▸</span></span>
      <svg width="60" height="60" viewBox="0 0 60 60" style="left:116px;top:24px" aria-hidden="true" fill="none" stroke="var(--gold)" stroke-width="3">
        <rect x="14" y="18" width="26" height="38" rx="13"/><line x1="27" y1="18" x2="27" y2="32"/><path d="M27 18C27 8 40 10 48 4"/>
      </svg>
    </a>
    <a class="promo promo-party" href="#">
      <span class="promo-label"><span class="small">We've got a</span><span class="big">Free</span><span class="mid">Party Room</span><span class="cta">Learn more ▸</span></span>
      <svg width="60" height="70" viewBox="0 0 60 70" style="left:168px;top:22px" aria-hidden="true" fill="none" stroke="var(--gold)" stroke-width="3">
        <path d="M6 6H26C26 22 22 30 16 30 10 30 6 22 6 6Z"/><line x1="16" y1="30" x2="16" y2="60"/><line x1="8" y1="60" x2="24" y2="60"/>
        <path d="M34 18H52C52 32 48 38 43 38 38 38 34 32 34 18Z"/><line x1="43" y1="38" x2="43" y2="60"/><line x1="36" y1="60" x2="50" y2="60"/>
      </svg>
    </a>
    <a class="promo promo-specials" href="#">
      <span class="promo-label" style="top:22px"><span class="name">Brunello's</span><span class="mid">Specials</span><span class="cta">click here ▸</span></span>
      <svg width="60" height="60" viewBox="0 0 64 64" style="left:142px;top:22px" aria-hidden="true">
        <circle cx="32" cy="32" r="30" fill="var(--gold)"/><circle cx="32" cy="32" r="20" fill="none" stroke="var(--red-deep)" stroke-width="2"/>
        <g stroke="var(--red-deep)" stroke-width="3" fill="none"><line x1="26" y1="18" x2="26" y2="46"/><line x1="22" y1="18" x2="22" y2="26"/><line x1="30" y1="18" x2="30" y2="26"/><path d="M38 46V18C42 22 42 30 38 32"/></g>
      </svg>
    </a>
  </div>

  <nav class="footer-nav">
    <a href="#">Home</a><a href="#">Menu</a><a href="#">Specials</a><a href="#">Coupons</a><a href="#">Locations</a><a href="#">Contact</a>
  </nav>
  <p class="copyright">Copyright © 2013 Brunello's Italian Restaurant</p>
  <address class="contact-block">
    <span class="contact-line">1842 Maple Hill Rd, Fairview, KY 40299-1100</span>
    <span class="contact-line">Phone: (555) 218-4470</span>
  </address>
</body>
</html>
```